Global Expert Network Firm needs business card design

We need business card design for a new company based in Seoul, South Korea called 'Corwell Insight Partners'. We recruit industry experts covering all countries and connect our client and recruited expert by phone, face-to-face meetings and etc. We are a global expert network firm that is focused on delivering high-quality experts to our clients throughout the world. Our clients include multinational corporations, global consulting firms, private equity firms, venture capital firms, asset management companies.
We have made new logo and please find attachment.(Please use new logo)
Target Market(s)
Global Consulting Firms, Investment Firms, Private Equity Firms, Venture Capital Firms.
Industry/Entity Type
Recruitment
Contact Information for Business Card
We need two Languages (English and Korean Version).
The front is Korean and the back is English version.
[The back] [English]
Company Name: Corwell Insight Partners, Inc.
CEO Name: Daniel Park
Address: #507, Hanbit Bldg, 82 Maebongsan-ro, Dobong-gu, Seoul, 01327, Korea
Tel. +82 2 718 4052
Fax. +82 2 864 1097
Mobile. +82 10 7264 8815
Email: daniel@corwellip.com
Web: www.corwellip.com
[The front] [Korean] => Described in same order as English version.
회사명: 코웰인사이트파트너스(주)
대표이사: 박도현
주소: 서울시 도봉구 매봉산로 82 한빛빌딩 507호
Tel. 02 718 4052
Fax. 02 864 1097
Mobile. 010 7264 8815
Web: www.corwellip.com
Look and feel
Each slider illustrates characteristics of the customer's brand and the style your logo design should communicate.

```html
<!DOCTYPE html>
<html lang="ko">
<head>
<meta charset="utf-8">
<title>Corwell Insight Partners — Business Cards</title>
<link rel="stylesheet" href="https://fonts.googleapis.com/css2?family=Arimo:wght@400;700&family=Noto+Sans+KR:wght@400;500&display=swap">
<style>
  :root {
    --brand-blue: #1461b4;
    --brand-gray: #a7a9ac;
    --ink: #2b2b2b;
    --rule: #9a9a9a;
    --paper: #ffffff;
    --backdrop: #e9eaec;
  }
  * { margin: 0; padding: 0; box-sizing: border-box; }
  html, body { width: 1200px; height: 1200px; overflow: hidden; background: var(--backdrop); }
  body { position: relative; font-family: "Arimo", "Noto Sans KR", Arial, sans-serif; color: var(--ink); }

  .card-slot { position: absolute; left: 235px; width: 730px; height: 445px; }
  .card-slot--front { top: 95px; }
  .card-slot--back { top: 630px; }

  .card {
    position: absolute; left: 0; top: 0;
    width: 905px; height: 552px;
    transform: scale(0.8066); transform-origin: top left;
    background: var(--paper);
    box-shadow: 0 14px 30px rgba(0,0,0,0.22);
    overflow: hidden;
  }
  .card__shapes { position: absolute; inset: 0; }

  .brand-mark {
    position: absolute; left: 69px; top: 70px; width: 194px; height: 194px;
    display: flex; flex-direction: column; justify-content: center; gap: 14px;
    padding-left: 14px;
  }
  .brand-mark__square { width: 30px; height: 30px; background: var(--brand-blue); }
  .brand-mark__name {
    color: var(--brand-blue); font-weight: 700; font-size: 29px; line-height: 1.15;
    text-transform: uppercase; letter-spacing: 0.5px;
  }

  .person { position: absolute; left: 610px; top: 265px; }
  .person__name { font-weight: 700; font-size: 28px; letter-spacing: 0.3px; text-transform: uppercase; }
  .person__title { color: var(--brand-blue); font-weight: 700; font-size: 19px; margin-top: 2px; }
  .person__contact { position: absolute; left: 609px; top: 337px; font-size: 17.5px; line-height: 22px; }
  .label { color: var(--brand-blue); font-weight: 700; }

  .company { position: absolute; left: 40px; width: 550px; top: 380px; text-align: center; }
  .company__name { color: var(--brand-blue); font-weight: 700; font-size: 31px; white-space: nowrap; }
  .company__details { font-size: 18px; line-height: 26px; margin-top: 6px; }
  .company__details--kr { font-family: "Noto Sans KR", "Arimo", sans-serif; font-size: 18.5px; line-height: 27px; }
  .company__lines { font-size: 17.5px; line-height: 21px; margin-top: 6px; }
  .company__phones { font-size: 17.5px; margin-top: 8px; white-space: nowrap; }
  .company__details--kr + .company__phones { margin-top: 2px; }
</style>
</head>
<body>

<!-- Korean side -->
<div class="card-slot card-slot--front">
  <article class="card" lang="ko">
    <svg class="card__shapes" viewBox="0 0 905 552" aria-hidden="true">
      <polygon points="408,0 528,0 0,320 0,245" fill="var(--brand-gray)"/>
      <polygon points="905,287 905,345 565,552 470,552" fill="var(--brand-gray)"/>
      <rect x="30" y="30" width="846" height="492" fill="var(--paper)" stroke="#e2e2e2" stroke-width="2"/>
      <polygon points="0,0 408,0 0,245" fill="var(--brand-blue)"/>
      <polygon points="36,37 322,37 36,210" fill="var(--brand-gray)"/>
      <polygon points="565,552 905,552 905,345" fill="var(--brand-blue)"/>
      <polygon points="637,522 876,522 876,378" fill="var(--brand-gray)"/>
      <rect x="55" y="58" width="220" height="206" fill="var(--paper)"/>
      <line x1="593" y1="263" x2="593" y2="488" stroke="var(--rule)" stroke-width="1.5"/>
      <line x1="575" y1="327" x2="865" y2="327" stroke="var(--rule)" stroke-width="1.5"/>
    </svg>

    <div class="brand-mark">
      <span class="brand-mark__square"></span>
      <span class="brand-mark__name">Corwell<br>Insight<br>Partners</span>
    </div>

    <div class="person">
      <div class="person__name">Daniel Park</div>
      <div class="person__title">CEO</div>
    </div>
    <div class="person__contact">
      <div><span class="label">M</span>: +010 7264 8815</div>
      <div><span class="label">E</span>: daniel@corwellip.com</div>
    </div>

    <div class="company">
      <div class="company__name">CORWELL INSIGHT PARTNERS, Inc.</div>
      <div class="company__details company__details--kr">
        <div>회사명: 코웰인사이트파트너스(주) 대표이사: 박도현</div>
        <div>주소: 서울시 도봉구 매봉산로 82 한빛빌딩 507호</div>
      </div>
      <div class="company__phones"><span class="label">T</span>: 02 718 4052&nbsp; <span class="label">F</span>: 02 864 1097&nbsp; <span class="label">W</span>: www.corwellip.com</div>
    </div>
  </article>
</div>

<!-- English side -->
<div class="card-slot card-slot--back">
  <article class="card" lang="en">
    <svg class="card__shapes" viewBox="0 0 905 552" aria-hidden="true">
      <polygon points="408,0 528,0 0,320 0,245" fill="var(--brand-gray)"/>
      <polygon points="905,287 905,345 565,552 470,552" fill="var(--brand-gray)"/>
      <rect x="30" y="30" width="846" height="492" fill="var(--paper)" stroke="#e2e2e2" stroke-width="2"/>
      <polygon points="0,0 408,0 0,245" fill="var(--brand-blue)"/>
      <polygon points="36,37 322,37 36,210" fill="var(--brand-gray)"/>
      <polygon points="565,552 905,552 905,345" fill="var(--brand-blue)"/>
      <polygon points="637,522 876,522 876,378" fill="var(--brand-gray)"/>
      <rect x="55" y="58" width="220" height="206" fill="var(--paper)"/>
      <line x1="593" y1="263" x2="593" y2="488" stroke="var(--rule)" stroke-width="1.5"/>
      <line x1="575" y1="327" x2="865" y2="327" stroke="var(--rule)" stroke-width="1.5"/>
    </svg>

    <div class="brand-mark">
      <span class="brand-mark__square"></span>
      <span class="brand-mark__name">Corwell<br>Insight<br>Partners</span>
    </div>

    <div class="person">
      <div class="person__name">Daniel Park</div>
      <div class="person__title">CEO</div>
    </div>
    <div class="person__contact">
      <div><span class="label">M</span>: +82 10 7264 8815</div>
      <div><span class="label">E</span>: daniel@corwellip.com</div>
    </div>

    <div class="company">
      <div class="company__name">CORWELL INSIGHT PARTNERS, Inc.</div>
      <div class="company__lines">
        <div>#507, Hanbit Bldg, 82 Maebongsan-ro,</div>
        <div>Dobong-gu, Seoul, 01327, Korea</div>
      </div>
      <div class="company__phones"><span class="label">T</span>: +82 2 718 4052&nbsp; <span class="label">F</span>: +82 2 864 1097&nbsp; <span class="label">W</span>: www.corwellip.com</div>
    </div>
  </article>
</div>

</body>
</html>
```